Business card design for Healthcare Clinic

Need to create an elegant business card design that incorporates a QR code to a specific page on the website

Industry/Entity Type

Healthcare

Contact Information for Business Card

Name, job title, address, phone number, fax number, website

Font styles to use
Serif
Sans Serif

Colors
0054AA
0677BA
7BADD7
CADEEF
E8F1F8
0094D4
00A9DD
6FCCEA
C7EBF8
E9F6FB
6B429C
8869AF
B7A5CE
E3DAEB
F3F0F8

Requirements
Must have
• QR Code on the back side that will link to a specific website page (use place holder for now)
Nice to have
• Maybe try to incorporate the logo design elements (DNA strand) into the design. Please inquire for website if you want to see.

```html
<!DOCTYPE html>
<html lang="en">
<head>
<meta charset="utf-8">
<title>Harbor Point Regenerative Clinic – Business Card</title>
<link rel="stylesheet" href="https://fonts.googleapis.com/css2?family=Noto+Serif:wght@400;700&family=Open+Sans:wght@400;600&display=swap">
<style>
  :root {
    --bg: #d6d4d6;
    --brand-blue: #0094D4;
    --pale: #E9F6FB;
    --navy: #2a2f78;
    --helix: #CADEEF;
    --white: #ffffff;
    --white-soft: rgba(255,255,255,0.88);
  }
  * { box-sizing: border-box; margin: 0; padding: 0; }
  html, body { width: 1200px; height: 900px; overflow: hidden; }
  body {
    background: var(--bg);
    font-family: "Noto Serif", Georgia, serif;
    display: flex;
    flex-direction: column;
    align-items: center;
    justify-content: center;
    gap: 48px;
  }
  .card {
    position: relative;
    width: 640px;
    height: 366px;
    background: var(--brand-blue);
    box-shadow: 0 10px 28px rgba(0,0,0,0.18);
    overflow: hidden;
  }

  /* Front */
  .front__header {
    position: absolute;
    left: 0; top: 0;
    width: 420px; height: 150px;
    background: var(--pale);
  }
  .front__helix {
    position: absolute;
    right: 0; top: 0;
    width: 150px; height: 72px;
    background: linear-gradient(135deg, var(--pale) 20%, var(--helix) 60%, var(--pale) 95%);
    opacity: 0.8;
  }
  .brand {
    position: absolute;
    left: 36px; top: 96px;
    display: flex; align-items: center; gap: 10px;
    font-weight: 700;
    font-size: 18px;
    color: var(--navy);
    white-space: nowrap;
  }
  .brand__dot {
    width: 10px; height: 10px; border-radius: 50%;
    background: currentColor;
  }
  .person {
    position: absolute;
    left: 36px; top: 176px;
    color: var(--white);
  }
  .person__name { font-size: 20px; font-weight: 700; }
  .person__title { font-size: 12px; color: var(--white-soft); margin-top: 4px; }
  .address {
    position: absolute;
    left: 36px; top: 246px;
    display: flex; gap: 12px;
    color: var(--white-soft);
    font-size: 11.5px; line-height: 1.5;
    width: 330px;
  }
  .address svg { flex: none; margin-top: 2px; }
  .contacts {
    position: absolute;
    left: 444px; top: 40px;
    list-style: none;
    color: var(--white-soft);
    font-size: 11.5px;
  }
  .contacts li {
    display: flex; align-items: center; gap: 12px;
    margin-bottom: 22px;
    white-space: nowrap;
  }
  .contacts svg { flex: none; }

  /* Back */
  .back {
    display: flex; flex-direction: column;
    align-items: center; justify-content: center;
    gap: 34px;
  }
  .back .brand {
    position: static;
    color: var(--white);
    font-size: 26px;
  }
  .back__web {
    font-size: 16px;
    color: var(--white);
  }
  .back__qr {
    position: absolute;
    right: 36px; bottom: 36px;
    width: 84px; height: 84px;
    background: var(--white);
    border-radius: 4px;
  }
</style>
</head>
<body>

  <section class="card front" aria-label="Card front">
    <div class="front__header">
      <div class="front__helix" role="img" aria-label="Faint DNA strand decoration"></div>
      <div class="brand"><span class="brand__dot"></span>Harbor Point Regenerative Clinic</div>
    </div>

    <div class="person">
      <p class="person__name">Mara Ellison</p>
      <p class="person__title">Marketing Coordinator</p>
    </div>

    <div class="address">
      <svg width="14" height="18" viewBox="0 0 14 18" aria-hidden="true">
        <path d="M7 0a6 6 0 0 0-6 6c0 4.5 6 11 6 11s6-6.5 6-11a6 6 0 0 0-6-6z" fill="#fff"/>
        <circle cx="7" cy="6" r="2.2" fill="#0094D4"/>
      </svg>
      <p>Lorem ipsum dolor sit amet, consectetur adipiscing elit, sed do eiusmod tempor incididunt ut labore et dolore magna aliqua.</p>
    </div>

    <ul class="contacts">
      <li>
        <svg width="12" height="10" viewBox="0 0 12 10" aria-hidden="true"><rect x="0.5" y="0.5" width="11" height="9" fill="#fff"/><path d="M0.5 0.5 6 5l5.5-4.5" stroke="#0094D4" fill="none"/></svg>
        m.ellison@mailbox.com
      </li>
      <li>
        <svg width="12" height="10" viewBox="0 0 12 10" aria-hidden="true"><rect x="0" y="0" width="12" height="10" rx="1" fill="#fff"/><rect x="2" y="2" width="4" height="6" fill="#0094D4"/></svg>
        214 555 0148
      </li>
      <li>
        <svg width="12" height="12" viewBox="0 0 12 12" aria-hidden="true"><path d="M2 0h2.5l1 3-1.5 1.2a7 7 0 0 0 3.8 3.8L9 6.5l3 1V10a2 2 0 0 1-2 2A10 10 0 0 1 0 2a2 2 0 0 1 2-2z" fill="#fff"/></svg>
        205 555 0163
      </li>
      <li>
        <svg width="12" height="12" viewBox="0 0 12 12" aria-hidden="true"><circle cx="6" cy="6" r="5.4" fill="none" stroke="#fff"/><ellipse cx="6" cy="6" rx="2.3" ry="5.4" fill="none" stroke="#fff"/><path d="M0.6 6h10.8" stroke="#fff"/></svg>
        www.harborpointclinic.com
      </li>
    </ul>
  </section>

  <section class="card back" aria-label="Card back">
    <div class="brand"><span class="brand__dot"></span>Harbor Point Regenerative Clinic</div>
    <p class="back__web">www.harborpointclinic.com</p>
    <div class="back__qr" role="img" aria-label="QR code placeholder linking to a clinic web page"></div>
  </section>

</body>
</html>
```